Flyer for the Lumen 2025 Conference

I am looking to produce a flyer for our upcoming conference, Lumen 2025. This is an annual conference that we plan to publicize on social media. The ideal designer will create a flyer that is eye-catching and effectively communicates the key information. Please see attached our logo, speaker photo, and flyer content.

Target Market(s)

All demographics

Industry/Entity Type

Christian

Font styles to use
Sans Serif

Requirements
Should not have
• Cross, church

```html
<!DOCTYPE html>
<html lang="en">
<head>
<meta charset="utf-8">
<title>Lumen 2025 Conference</title>
<link rel="stylesheet" href="https://fonts.googleapis.com/css2?family=Bebas+Neue&family=Montserrat:wght@400;600;700;800&family=Allura&display=swap">
<style>
  :root {
    --sky-top: #3c4a55;
    --sky-mid: #56687a;
    --city-dark: #1f272e;
    --city-mid: #3a444c;
    --white: #ffffff;
    --yellow: #f7c80f;
    --ink: #111111;
    --panel: #dcdcdc;
    --suit: #1f5fb4;
  }
  * { margin: 0; padding: 0; box-sizing: border-box; }
  html, body { width: 927px; height: 1200px; overflow: hidden; background: var(--city-dark); }
  .flyer {
    position: relative; width: 927px; height: 1200px; overflow: hidden;
    font-family: "Montserrat", sans-serif; color: var(--white);
  }
  .backdrop {
    position: absolute; inset: 0;
    background:
      radial-gradient(ellipse 180px 60px at 530px 290px, rgba(190,180,230,0.55), transparent 70%),
      linear-gradient(180deg, var(--sky-top) 0%, var(--sky-mid) 22%, #4a5866 38%, var(--city-mid) 55%, var(--city-dark) 100%);
  }
  .brand {
    position: absolute; left: 606px; top: 84px;
    font-weight: 700; font-size: 58px; letter-spacing: 1px; line-height: 1;
    color: var(--white);
  }
  .title {
    position: absolute; left: 103px; top: 128px;
    font-family: "Bebas Neue", sans-serif; font-size: 182px; line-height: 138px;
    color: var(--white); letter-spacing: 2px; z-index: 2;
  }
  .tagline {
    position: absolute; left: 86px; top: 412px; z-index: 3;
    font-family: "Allura", cursive; font-size: 64px; line-height: 1;
    color: var(--yellow); transform: rotate(-3deg); transform-origin: left;
    white-space: nowrap;
  }
  .speaker-photo {
    position: absolute; left: 605px; top: 354px; width: 300px; height: 500px; z-index: 1;
    border-radius: 40% 40% 8px 8px / 28% 28% 8px 8px;
    background: linear-gradient(180deg, #5b4636 0%, #7b8a82 28%, var(--suit) 45%, #174a8e 100%);
    opacity: 0.92;
  }
  .schedule { position: absolute; left: 99px; top: 567px; z-index: 2; }
  .session { position: relative; height: 140px; }
  .session .cal { position: absolute; left: 0; top: 0; width: 51px; height: 50px; }
  .session .clock { position: absolute; left: 0; top: 62px; width: 50px; height: 50px; }
  .session .day {
    position: absolute; left: 72px; top: 0; font-weight: 800; font-size: 31px;
    color: var(--yellow); letter-spacing: 0.5px; line-height: 1;
  }
  .session .date, .session .time {
    position: absolute; left: 72px; font-weight: 400; font-size: 24px; letter-spacing: 0.5px;
    white-space: nowrap; line-height: 1;
  }
  .session .date { top: 40px; }
  .session .time { top: 78px; }
  .speaker-card { position: absolute; left: 555px; top: 807px; width: 288px; height: 150px; z-index: 2; }
  .speaker-card .panel { position: absolute; inset: 0; background: var(--panel); border-radius: 14px; border: 2px solid #f2f2f2; }
  .speaker-card .label {
    position: absolute; left: 3px; top: 3px; width: 282px; height: 48px;
    background: var(--yellow); border-radius: 24px; border: 2px solid #fff;
    color: var(--ink); font-weight: 700; font-size: 30px; text-align: center; line-height: 44px;
  }
  .speaker-card .name {
    position: absolute; left: 0; right: 0; top: 74px; color: var(--ink);
    font-weight: 800; font-size: 22px; text-align: center; line-height: 26px; letter-spacing: 0.5px;
  }
  .contact { position: absolute; left: 99px; top: 1030px; }
  .contact-row { position: relative; display: flex; align-items: center; gap: 16px; }
  .contact-row svg { width: 27px; height: 27px; flex: none; }
  .contact-row.phone { font-weight: 700; font-size: 28px; height: 34px; }
  .contact-row.email { font-weight: 700; font-size: 20px; margin-top: 6px; height: 30px; }
  .contact-row.web { font-weight: 700; font-size: 20px; margin-top: 6px; height: 30px; text-decoration: underline; }
  .venue-pin { position: absolute; left: 495px; top: 1026px; width: 72px; height: 110px; }
  .venue {
    position: absolute; left: 579px; top: 1026px; font-weight: 700; font-size: 18.5px; line-height: 28px;
    white-space: nowrap;
  }
</style>
</head>
<body>
<div class="flyer">
  <div class="backdrop" role="img" aria-label="Aerial view of a city street lined with tall buildings under a cloudy dusk sky"></div>

  <div class="brand">KAVRIN</div>

  <div class="speaker-photo" role="img" aria-label="Photo of the speaker in a blue suit, seated"></div>

  <h1 class="title">LUMEN<br>2025</h1>
  <div class="tagline">The Voice Of The Lord</div>

  <div class="schedule">
    <div class="session">
      <svg class="cal" viewBox="0 0 51 50"><rect x="1" y="8" width="49" height="41" rx="6" fill="#f7c80f"/><circle cx="15" cy="7" r="4" fill="none" stroke="#f7c80f" stroke-width="3"/><circle cx="36" cy="7" r="4" fill="none" stroke="#f7c80f" stroke-width="3"/></svg>
      <svg class="clock" viewBox="0 0 50 50"><circle cx="25" cy="25" r="22" fill="none" stroke="#f7c80f" stroke-width="4"/><path d="M25 12V26L34 32" fill="none" stroke="#f7c80f" stroke-width="4" stroke-linecap="round"/></svg>
      <div class="day">FRIDAY</div>
      <div class="date">26 DECEMBER&nbsp; 2025</div>
      <div class="time">6:30PM - 9:00PM</div>
    </div>
    <div class="session">
      <svg class="cal" viewBox="0 0 51 50"><rect x="1" y="8" width="49" height="41" rx="6" fill="#f7c80f"/><circle cx="15" cy="7" r="4" fill="none" stroke="#f7c80f" stroke-width="3"/><circle cx="36" cy="7" r="4" fill="none" stroke="#f7c80f" stroke-width="3"/></svg>
      <svg class="clock" viewBox="0 0 50 50"><circle cx="25" cy="25" r="22" fill="none" stroke="#f7c80f" stroke-width="4"/><path d="M25 12V26L34 32" fill="none" stroke="#f7c80f" stroke-width="4" stroke-linecap="round"/></svg>
      <div class="day">SATURDAY</div>
      <div class="date">27 DECEMBER&nbsp; 2025</div>
      <div class="time">5:30PM - 8:00PM</div>
    </div>
    <div class="session">
      <svg class="cal" viewBox="0 0 51 50"><rect x="1" y="8" width="49" height="41" rx="6" fill="#f7c80f"/><circle cx="15" cy="7" r="4" fill="none" stroke="#f7c80f" stroke-width="3"/><circle cx="36" cy="7" r="4" fill="none" stroke="#f7c80f" stroke-width="3"/></svg>
      <svg class="clock" viewBox="0 0 50 50"><circle cx="25" cy="25" r="22" fill="none" stroke="#f7c80f" stroke-width="4"/><path d="M25 12V26L34 32" fill="none" stroke="#f7c80f" stroke-width="4" stroke-linecap="round"/></svg>
      <div class="day">SUNDAY</div>
      <div class="date">29 DECEMBER&nbsp; 2025</div>
      <div class="time">4:30PM - 7:00PM</div>
    </div>
  </div>

  <div class="speaker-card">
    <div class="panel"></div>
    <div class="label">Speaker</div>
    <div class="name">PROPHET ELIAS<br>MORENO</div>
  </div>

  <div class="contact">
    <div class="contact-row phone">
      <svg viewBox="0 0 27 27"><circle cx="13.5" cy="13.5" r="13.5" fill="#f7c80f"/><path d="M8.5 7c1-.6 1.8-.3 2.3.6l1 2c.3.7.1 1.3-.5 1.8l-.7.5c.8 1.8 2 3 3.8 3.8l.5-.7c.5-.6 1.1-.8 1.8-.5l2 1c.9.5 1.2 1.3.6 2.3-1 1.6-2.6 2-4.3 1.3-3.2-1.4-5.6-3.8-7-7C7.3 9.6 7.3 7.9 8.5 7z" fill="#111"/></svg>
      <span>555 014 2270</span>
    </div>
    <div class="contact-row email">
      <svg viewBox="0 0 27 27"><circle cx="13.5" cy="13.5" r="13.5" fill="#f7c80f"/><rect x="7" y="9" width="13" height="9" fill="none" stroke="#111" stroke-width="1.6"/><path d="M7 9l6.5 5 6.5-5" fill="none" stroke="#111" stroke-width="1.6"/></svg>
      <span>hello@kavrin.org</span>
    </div>
    <div class="contact-row web">
      <svg viewBox="0 0 27 27"><circle cx="13.5" cy="13.5" r="13.5" fill="#f7c80f"/><circle cx="13.5" cy="13.5" r="6.5" fill="none" stroke="#111" stroke-width="1.4"/><ellipse cx="13.5" cy="13.5" rx="3" ry="6.5" fill="none" stroke="#111" stroke-width="1.2"/><path d="M7 13.5h13" stroke="#111" stroke-width="1.2"/></svg>
      <span>www.kavrin.org</span>
    </div>
  </div>

  <svg class="venue-pin" viewBox="0 0 72 110"><ellipse cx="36" cy="98" rx="36" ry="11" fill="#d6d6d6"/><path d="M36 2C19 2 6 15 6 32c0 22 30 62 30 62s30-40 30-62C66 15 53 2 36 2z" fill="#f7c80f"/><circle cx="36" cy="32" r="12" fill="#2a3138"/></svg>
  <div class="venue">The Harborview<br>Performing Arts Center<br>128 Lindenfield Street<br>Ashford, Maine 04000</div>
</div>
</body>
</html>
```